Electrical Contractor Company Profile

We need a Brochure that is more entertaining than our current Company Profile Document. We have lots of great experience and awesome looking jobs in our portfolio but need a document that we can either print of send in electronic format to accompany some of our submissions.

We are ideally looking for something 9-10 pages in A4 with some of the pages opening out to A3.

We are looking for a document that is professional and smart however shows the colour and quality that we feel we offer to prospective clientele.

I have included the current Company Profile and Logo along with a number of images of completed projects that may be of use.

Target Market(s)

Builders, Facility Managers, Engineers, Decision makers

Industry/Entity Type

Electrical

Font styles to use
Sans Serif

Colors

Designer to choose colors to be used in the design.

Requirements
Must have
• - Modern look with a focus on sustainability
• - Clean Simple and Professional
• - Incorporate our Logo
• Core Business Lines need to be across an A3 opening page and have photos relating to these lines Solar, Communications and any of the projects.
Nice to have
• Lots of colour and photos mixed with the text
Should not have
• Lightning bolts or corny symbols

```html
<!DOCTYPE html>
<html lang="en">
<head>
<meta charset="UTF-8">
<title>Lumen Electrical Technology – Core Business Spread</title>
<link href="https://fonts.googleapis.com/css2?family=Open+Sans:ital,wght@0,400;0,600;1,400;1,600&family=Play:wght@400&display=swap" rel="stylesheet">
<style>
  :root {
    --backdrop: #8a8a8a;
    --paper: #ffffff;
    --accent: #e4631f;
    --text: #4d4d4d;
    --text-dark: #2a2a2a;
    --logo-white: #ffffff;
    --fold-shadow: rgba(0,0,0,0.12);
  }
  * { box-sizing: border-box; margin: 0; padding: 0; }
  html, body { width: 1200px; height: 800px; overflow: hidden; }
  body {
    background: var(--backdrop);
    font-family: "Open Sans", Arial, sans-serif;
    color: var(--text);
  }
  .spread {
    position: absolute;
    left: 50px; top: 11px;
    width: 1100px; height: 778px;
    display: flex;
    background: var(--paper);
  }
  .page {
    position: relative;
    width: 550px; height: 778px;
    overflow: hidden;
    background: var(--paper);
  }
  .page--left::after {
    content: "";
    position: absolute; right: 0; top: 0; bottom: 0; width: 18px;
    background: linear-gradient(to left, var(--fold-shadow), transparent);
  }
  .page--right::before {
    content: "";
    position: absolute; left: 0; top: 0; bottom: 0; width: 18px;
    background: linear-gradient(to right, var(--fold-shadow), transparent);
    z-index: 3;
  }
  .hero-photo {
    position: absolute; left: 0; top: 0; width: 550px;
  }
  .page--left .hero-photo {
    height: 485px;
    background: linear-gradient(100deg, #b07a3e 0%, #d4a063 22%, #7a5a3a 40%, #e8e4e6 58%, #5a4a6e 78%, #3a3248 100%);
  }
  .page--right .hero-photo {
    height: 470px;
    background: linear-gradient(100deg, #6a6a78 0%, #7a5ca8 18%, #e0572a 34%, #3a3a4e 52%, #2e3560 72%, #1e1e26 100%);
  }
  .brand {
    position: absolute; top: 36px;
    display: flex; align-items: center; gap: 10px;
    z-index: 2;
  }
  .page--left .brand { left: 34px; }
  .page--right .brand { left: 325px; }
  .brand__mark {
    width: 34px; height: 34px; border-radius: 50%;
    border: 2px solid var(--logo-white);
  }
  .brand__name {
    font-family: "Open Sans", Arial, sans-serif;
    font-weight: 600;
    color: var(--logo-white);
    font-size: 20px; line-height: 1.05;
    letter-spacing: 0.5px;
  }
  .brand__name small { display: block; font-size: 12px; letter-spacing: 0.3px; }
  .text-panel {
    position: absolute; background: var(--paper);
    padding: 26px 24px 20px 26px;
    z-index: 2;
  }
  .page--left .text-panel { left: 268px; top: 160px; width: 282px; bottom: 0; }
  .page--right .text-panel { left: 22px; top: 150px; width: 282px; bottom: 0; padding-top: 20px; }
  .panel-title {
    font-family: "Play", Arial, sans-serif;
    color: var(--accent);
    font-size: 18px; letter-spacing: 2px;
    margin-bottom: 12px;
  }
  .panel-intro { font-size: 9.6px; line-height: 1.3; margin-bottom: 10px; }
  .business-lines { list-style: none; counter-reset: line; }
  .business-lines li {
    font-size: 9.6px; line-height: 1.3;
    text-align: justify;
    padding-left: 14px; position: relative;
    margin-bottom: 12px;
  }
  .business-lines li::before {
    content: attr(data-num) ".";
    position: absolute; left: 0; top: 0;
    color: var(--accent);
  }
  .business-lines .line-name { color: var(--accent); }
  .project-photo { position: absolute; z-index: 2; }
  .page--left .project-photo {
    left: 38px; top: 498px; width: 244px; height: 104px;
    background: linear-gradient(180deg, #c8d4de 0%, #e6e6e6 45%, #8a9a8c 75%, #5b7a4a 100%);
  }
  .page--right .project-photo {
    left: 284px; top: 480px; width: 212px; height: 128px;
    background: linear-gradient(90deg, #e8741e 0%, #f08a2a 30%, #9a9a9a 50%, #d8823a 72%, #c8c0b4 100%);
  }
  .testimonial {
    position: absolute; z-index: 2;
    font-size: 9.2px; line-height: 1.35; font-style: italic;
    color: var(--text-dark);
  }
  .page--left .testimonial { left: 38px; top: 614px; width: 250px; }
  .page--right .testimonial { left: 284px; top: 620px; width: 220px; font-size: 8.4px; }
  .testimonial cite { display: block; font-weight: 600; font-style: italic; }
</style>
</head>
<body>
  <main class="spread">
    <section class="page page--left">
      <div class="hero-photo" role="img" aria-label="Office interior with tall timber batten columns and patterned carpet"></div>
      <div class="brand">
        <span class="brand__mark"></span>
        <span class="brand__name">LUMEN<small>electrical technology</small></span>
      </div>

      <div class="text-panel">
        <h1 class="panel-title">CORE BUSINESS</h1>
        <p class="panel-intro">Lumen Electrical Technology maintains five core lines of business:</p>
        <ol class="business-lines">
          <li data-num="1"><span class="line-name">Breakdown and response</span> – providing a 24/7 call out service to a number of high profile clients this team is high energy and responsive to most situations. Consistently preforming at the top level of our clients expectations have resulted in excellent growth in this sector.</li>
          <li data-num="2"><span class="line-name">Planned Maintenance</span> – This team service over 500 sites across the Perth metropolitan area. Carrying out planned testing and repair of all electrical infrastructure required by our clients. This includes RCD and Emergency lighting along with thermographic surveys amongst many other services.</li>
          <li data-num="3"><span class="line-name">Communications</span> – our staff are extremely experienced and the majority carry Open Cabling licenses &amp; Certificate III qualifications in Telecommunications. The company own substantial amounts of specialized test equipment and regularly invest in continued training of staff. LET can supply both design and installation services for private networks. Providing a certified solution to any copper and fiber optic needs.</li>
        </ol>
      </div>

      <div class="project-photo" role="img" aria-label="Modern sports institute building with white curved facade and landscaped entry"></div>
      <blockquote class="testimonial">
        “The finished product at the Coastal Sports Institute was of excellent quality. We were extremely impressed with the ease of use and high levels of communication we received.”
        <cite>Daniel Marsh, Harbour Build Group</cite>
      </blockquote>
    </section>

    <section class="page page--right">
      <div class="hero-photo" role="img" aria-label="Lounge corridor with bold orange and purple fan mural, navy bench seating and timber slat wall"></div>
      <div class="brand">
        <span class="brand__mark"></span>
        <span class="brand__name">LUMEN<small>electrical technology</small></span>
      </div>

      <div class="text-panel">
        <ol class="business-lines">
          <li data-num="4"><span class="line-name">Electrical Projects</span> – this line of business is responsible for completing contracts both considered minor and major in value. Team members are experienced in installing various types of electrical systems and are well equipped in producing the high quality workmanship expected in this highly competitive sector.</li>
          <li data-num="5"><span class="line-name">Solar PV</span> – Focusing on the commercial market we are able to offer fully design solutions for photovoltaic systems up to 200KW designed to suit a client’s needs and budgets. With highly trained and experienced consultants and installers we pride ourselves on offering great value for money and clarity on project benefits.</li>
          <li data-num="6"><span class="line-name">Technology Services</span> – With great base knowledge and an ongoing commitment to training and innovation, LET are able to offer solutions for Energy Management, Energy Conservation, Electronic Lighting Control, Premise’s performance auditing and Power monitoring. Providing our clients with valuable expertise in reduction of running costs and better understanding of their assets maintenance requirements, producing ongoing savings in operation and replacement of plant.</li>
        </ol>
      </div>

      <div class="project-photo" role="img" aria-label="Orange electrical switchboard cabinets with wiring and control panels"></div>
      <blockquote class="testimonial">
        “The finished product is of excellent quality, and we have been extremely impressed with the ease of use and high levels of communication received.”
        <cite>Paul Kenner, Westgate Property Tower</cite>
      </blockquote>
    </section>
  </main>
</body>
</html>
```